Store Promo Card (already have logo!)

I need a card design (single side) for my online women’s gift shop containing a promotional code to be placed in bags for attendees at an event. I’m flexible on both shape and sizing, but perhaps a 4x6 card.
—It should contain my attached logo, my website (www.merrowlyn.com), and my Instagram handle (@merrowlyn) and promotion language such as “15% off your purchase with code: PIVRAL”.
—I think I would like my logo to be large.
—It should be clean, simple and modern in design and should use the colors from my logo.
—I would like about 3-5 product pictures depending on design.
Target Market(s)
Women ages 30 to 60
Industry/Entity Type
Retail Upscale Gift

```html
<!DOCTYPE html>
<html lang="en">
<head>
<meta charset="utf-8">
<title>Merrowlyn Promo Card</title>
<link rel="stylesheet" href="https://fonts.googleapis.com/css2?family=Playfair+Display:wght@700;900&family=Tinos:wght@400;700&display=swap">
<style>
  :root {
    --blush: #f2d7d3;
    --charcoal: #3d4543;
    --paper: #ffffff;
    --stage: #e4e5ea;
    --icon-rose: #b08a80;
  }
  html, body {
    margin: 0;
    padding: 0;
    width: 783px;
    height: 1200px;
    overflow: hidden;
    background: var(--stage);
  }
  .canvas {
    position: relative;
    width: 783px;
    height: 1200px;
  }
  .promo-card {
    position: absolute;
    left: 30px;
    top: 359px;
    width: 723px;
    height: 482px;
    display: block;
  }
  .brand-name {
    font-family: "Playfair Display", serif;
    font-weight: 700;
    fill: var(--charcoal);
  }
  .offer-headline {
    font-family: "Playfair Display", serif;
    font-weight: 900;
    fill: var(--charcoal);
  }
  .offer-copy,
  .contact-line {
    font-family: "Tinos", serif;
    fill: var(--charcoal);
  }
  .promo-code {
    font-family: "Tinos", serif;
    font-weight: 700;
    fill: var(--charcoal);
    letter-spacing: 6px;
  }
</style>
</head>
<body>
<main class="canvas">
  <svg class="promo-card" viewBox="0 0 926 617" xmlns="http://www.w3.org/2000/svg">
    <defs>
      <clipPath id="card-bounds"><rect width="926" height="617"/></clipPath>
      <radialGradient id="jewel-tone" cx="50%" cy="50%" r="50%">
        <stop offset="0%" stop-color="#f3e6c4"/>
        <stop offset="100%" stop-color="#d9b25c"/>
      </radialGradient>
      <linearGradient id="pouch-tone" x1="0" y1="0" x2="1" y2="1">
        <stop offset="0%" stop-color="#eef1f3"/>
        <stop offset="45%" stop-color="#b79a98"/>
        <stop offset="100%" stop-color="#6e625f"/>
      </linearGradient>
      <linearGradient id="slipper-tone" x1="0" y1="0" x2="0" y2="1">
        <stop offset="0%" stop-color="#f1f1f3"/>
        <stop offset="100%" stop-color="#b7a9b5"/>
      </linearGradient>
      <radialGradient id="tray-tone" cx="50%" cy="50%" r="50%">
        <stop offset="0%" stop-color="#c9a36b"/>
        <stop offset="100%" stop-color="#6f5638"/>
      </radialGradient>
    </defs>

    <!-- card base -->
    <rect class="card-border" width="926" height="617" fill="var(--blush)"/>
    <rect class="card-panel" x="38" y="38" width="850" height="434" fill="var(--paper)"/>

    <!-- brand block -->
    <rect class="brand-block" x="75" y="70" width="385" height="150" fill="var(--blush)"/>
    <rect class="brand-frame" x="89" y="85" width="358" height="124" fill="none" stroke="var(--charcoal)" stroke-width="2"/>
    <text class="brand-name" x="268" y="162" font-size="42" text-anchor="middle">MERROWLYN</text>

    <!-- featured jewellery -->
    <g role="img" aria-label="Photo of a pair of gold flower-shaped stud earrings with crystals">
      <circle cx="577" cy="132" r="66" fill="url(#jewel-tone)"/>
      <circle cx="775" cy="132" r="66" fill="url(#jewel-tone)"/>
    </g>

    <!-- offer -->
    <text class="offer-headline" x="674" y="335" font-size="100" text-anchor="middle">15%<tspan font-size="66" dx="4">off</tspan></text>
    <text class="offer-copy" x="672" y="383" font-size="27" font-weight="700" text-anchor="middle">Your purchase with code:</text>
    <rect class="code-badge" x="556" y="400" width="234" height="46" fill="var(--blush)"/>
    <text class="promo-code" x="676" y="436" font-size="36" text-anchor="middle">PIVRAL</text>

    <!-- contact -->
    <text class="contact-line" x="673" y="510" font-size="32" text-anchor="middle">www.merrowlyn.com</text>
    <rect class="handle-strip" x="460" y="522" width="428" height="57" fill="var(--paper)"/>
    <circle class="social-dot" cx="572" cy="549" r="14" fill="var(--icon-rose)"/>
    <text class="contact-line" x="598" y="561" font-size="32">@merrowlyn</text>

    <!-- product photos -->
    <g clip-path="url(#card-bounds)">
      <circle cx="190" cy="468" r="212" fill="var(--blush)"/>
      <circle cx="190" cy="468" r="198" fill="url(#pouch-tone)" role="img" aria-label="Photo of a pink camouflage zip pouch"/>
      <circle cx="386" cy="362" r="78" fill="var(--blush)"/>
      <circle cx="386" cy="362" r="68" fill="url(#slipper-tone)" role="img" aria-label="Photo of fluffy pom-pom slippers"/>
      <circle cx="395" cy="507" r="96" fill="var(--blush)"/>
      <circle cx="395" cy="507" r="86" fill="url(#tray-tone)" role="img" aria-label="Photo of a round leopard print tray"/>
    </g>
  </svg>
</main>
</body>
</html>
```